Velmora Group
Velmora Financial
Velmora Group -
Creative Brief
Pirot Brekon
Partner
318 Elmwick Lane London E9 4PQ United Kingdom
Pbrekon@quillmesh.net
Company No. 5281947
Please provide an alternative design with the name Velmora Group instead of Velmora Financial
Just the logo

```html
<!DOCTYPE html>
<html lang="en">
<head>
<meta charset="utf-8">
<title>Velmora Group Stationery</title>
<link rel="stylesheet" href="https://fonts.googleapis.com/css2?family=Cinzel:wght@700&family=Open+Sans:wght@400;600&display=swap">
<style>
  :root {
    --bg: #e9eaec;
    --paper: #ffffff;
    --ink: #1b2a3d;
    --muted: #5a6472;
    --blue: #1f63b0;
    --blue-dark: #0d2c57;
    --charcoal: #1e1f22;
    --grey-mid: #9a9ca0;
    --faint: #eef0f3;
  }
  * { box-sizing: border-box; margin: 0; padding: 0; }
  html, body { width: 1200px; height: 701px; overflow: hidden; }
  body {
    background: var(--bg);
    position: relative;
    font-family: "Open Sans", sans-serif;
    color: var(--ink);
  }
  .sheet {
    position: absolute;
    background: var(--paper);
    box-shadow: 0 2px 6px rgba(0,0,0,.18);
    overflow: hidden;
  }
  .brand {
    font-family: "Cinzel", serif;
    font-weight: 700;
    color: var(--blue-dark);
    letter-spacing: .04em;
    display: flex;
    align-items: center;
    gap: 6px;
    white-space: nowrap;
  }
  .brand-square { width: 10px; height: 10px; background: var(--blue); flex: none; }
  .brand-light { color: #ffffff; }
  .brand-light .brand-square { background: #ffffff; }
  .small { font-size: 6.5px; line-height: 1.5; color: var(--muted); }
  .name { font-family: "Cinzel", serif; font-weight: 700; font-size: 9px; color: var(--ink); letter-spacing: .05em; }
  .role { font-size: 6.5px; font-style: italic; color: var(--muted); }
  .blue-bar { position: absolute; left: 0; right: 0; bottom: 0; height: 5px;
    background: linear-gradient(90deg, var(--blue-dark), var(--blue) 60%, #7fb0e4); }

  /* business cards */
  .card { width: 204px; height: 115px; }
  .card-front-name { left: 53px; top: 43px; }
  .card-back-details { left: 276px; top: 43px; }
  .card-white-brand { left: 53px; top: 178px; }
  .card-blue { left: 276px; top: 178px;
    background: radial-gradient(circle at 70% 40%, #3b86d6, var(--blue) 45%, var(--blue-dark)); }
  .card-dark { left: 53px; top: 314px;
    background: linear-gradient(90deg, var(--charcoal), #4a4c50 55%, #c9cacc); }
  .card-white-mark { left: 276px; top: 314px; }

  .card-front-name .name { position: absolute; right: 12px; top: 12px; text-align: right; }
  .card-front-name .role { position: absolute; right: 12px; top: 24px; }
  .card-front-name .brand { position: absolute; left: 12px; top: 52px; font-size: 9px; }
  .card-front-name .small { position: absolute; left: 120px; top: 52px; }

  .card-back-details .brand { position: absolute; left: 12px; top: 10px; font-size: 8px; }
  .card-back-details .name { position: absolute; right: 12px; top: 28px; }
  .card-back-details .role { position: absolute; right: 12px; top: 40px; }
  .card-back-details .small { position: absolute; left: 12px; top: 40px; }

  .centered { display: flex; align-items: center; justify-content: center; }
  .card-white-brand .brand, .card-blue .brand, .card-dark .brand, .card-white-mark .brand { font-size: 13px; }
  .card-white-mark .brand { color: var(--grey-mid); }

  /* letterheads */
  .letterhead { width: 312px; height: 403px; top: 43px; }
  .letterhead-left { left: 511px; }
  .letterhead-right { left: 840px; }
  .letterhead .brand { position: absolute; left: 24px; top: 22px; font-size: 11px; }
  .letterhead .small { position: absolute; left: 150px; top: 22px; }
  .letterhead-left .small { left: 24px; top: 42px; }
  .letterhead .watermark-block { position: absolute; right: 40px; bottom: 30px; width: 90px; height: 60px; background: var(--faint); }

  /* envelopes */
  .envelope { width: 422px; height: 209px; }
  .envelope-blue { left: 72px; top: 444px; }
  .envelope-white { left: 494px; top: 468px; height: 197px; }
  .flap { position: absolute; left: 0; top: 0; width: 100%; height: 60px; }
  .envelope .brand { position: absolute; left: 50%; top: 14px; transform: translateX(-50%); font-size: 11px; }
  .envelope .small { position: absolute; left: 24px; bottom: 24px; }
  .envelope .watermark-block { position: absolute; right: 60px; bottom: 24px; width: 80px; height: 54px; background: var(--faint); }
</style>
</head>
<body>

  <!-- business cards -->
  <div class="sheet card card-front-name">
    <div class="name">Pirot Brekon</div>
    <div class="role">Partner</div>
    <div class="brand"><span class="brand-square"></span>Velmora Group</div>
    <div class="small">318 Elmwick Lane<br>London E9 4PQ<br>Pbrekon@quillmesh.net</div>
    <div class="blue-bar"></div>
  </div>

  <div class="sheet card card-back-details">
    <div class="brand"><span class="brand-square"></span>Velmora Group</div>
    <div class="name">Pirot Brekon</div>
    <div class="role">Partner</div>
    <div class="small">318 Elmwick Lane<br>London E9 4PQ<br>United Kingdom<br>Company No. 5281947</div>
  </div>

  <div class="sheet card card-white-brand centered">
    <div class="brand"><span class="brand-square"></span>Velmora Group</div>
    <div class="blue-bar"></div>
  </div>

  <div class="sheet card card-blue centered">
    <div class="brand brand-light"><span class="brand-square"></span>Velmora Group</div>
  </div>

  <div class="sheet card card-dark centered">
    <div class="brand brand-light"><span class="brand-square"></span>Velmora Group</div>
  </div>

  <div class="sheet card card-white-mark centered">
    <div class="brand"><span class="brand-square"></span>Velmora Group</div>
  </div>

  <!-- letterheads -->
  <div class="sheet letterhead letterhead-left">
    <div class="brand"><span class="brand-square"></span>Velmora Group</div>
    <div class="small">318 Elmwick Lane London E9 4PQ<br>United Kingdom<br>Pbrekon@quillmesh.net</div>
    <div class="watermark-block"></div>
    <div class="blue-bar"></div>
  </div>

  <div class="sheet letterhead letterhead-right">
    <div class="brand"><span class="brand-square"></span>Velmora Group</div>
    <div class="small">318 Elmwick Lane London E9 4PQ<br>United Kingdom<br>Company No. 5281947</div>
    <div class="watermark-block"></div>
    <div class="blue-bar"></div>
  </div>

  <!-- envelopes -->
  <div class="sheet envelope envelope-blue">
    <svg class="flap" viewBox="0 0 422 60" preserveAspectRatio="none" aria-hidden="true">
      <defs>
        <linearGradient id="flap-blue" x1="0" x2="1">
          <stop offset="0" stop-color="#0d2c57"/>
          <stop offset=".5" stop-color="#1f63b0"/>
          <stop offset="1" stop-color="#0d2c57"/>
        </linearGradient>
      </defs>
      <path d="M0 0 H422 V34 L211 58 L0 34 Z" fill="url(#flap-blue)"/>
    </svg>
    <div class="brand brand-light"><span class="brand-square"></span>Velmora Group</div>
    <div class="small">318 Elmwick Lane London E9 4PQ<br>United Kingdom</div>
    <div class="watermark-block"></div>
    <div class="blue-bar"></div>
  </div>

  <div class="sheet envelope envelope-white">
    <svg class="flap" viewBox="0 0 422 60" preserveAspectRatio="none" aria-hidden="true">
      <path d="M0 0 H422 V30 L211 56 L0 30 Z" fill="#ffffff" stroke="#d5d8dd" stroke-width="1"/>
    </svg>
    <div class="brand"><span class="brand-square"></span>Velmora Group</div>
    <div class="small">318 Elmwick Lane London E9 4PQ<br>United Kingdom</div>
    <div class="watermark-block"></div>
    <div class="blue-bar"></div>
  </div>

</body>
</html>
```